Peptide Weight Loss Trifold

A trifold to market peptide weight loss injections. We are different than other clinics, in that we offer a three step approach to effortlessly lose weight and keep it off.

The peptides used are Semaglutide and AOD9604, both proven to . We also have Vitalis Core, a product that heals the gut biome and brain hormone response to weight loss. These three items stacked together is what sets us apart from other clinics. Both peptides are approved by the NHB for weight loss.

We also compound our peptides so they are much cheaper than the commercial Semaglutide also known as Lunavex, and Trelmo. These two commercial peptides from big pharma, each run about 1200.00 per month. Our compounded peptides are a fraction of that cost.
AOD9604....(Anti Obesity Drug)
Patients are losing as much weight as if they had bariatric surgery. 3-5 pounds per week.

If your are like 85% of dieters, its not your first time trying to get healthy and lose weight.
Join thousands of folks pushing the past plateaus and kill the cravings without starving via Quarlin MD's 16-Week program.
Five Star reviews.
"I have been on Semaglutide for one month. I guess the numbers are the crucial part of all semaglutide reviews. That’s it. I have dropped 16lbs. One of the things I have truly come to appreciate is that Sem will limit your appetite. " Marisol
"I’ve lost 13.5 pounds in a month, and I can’t even tell how it happened. The interesting part is that I don’t want to eat sweets anymore. I just want to eat less, I eat small portions while losing weight and enjoy my life." Tansy47
" I’ve been on the double peptide plan for a month and have dropped 20 pounds, despite not exercising. I’m delighted to see these figures change." Wendell
"Semaglutide worked for me. 10 out of 10." Gus

Hunger pangs! The primary roadblock to weight loss. With semaglutide, hunger pangs are a thing of the past. Semaglutide....changing the game!

Benefits of Semaglutide:
Reduces hunger pangs
Makes you feel fuller longer
Reduces food cravings
Reduces cardiovascular risk factors
Improves insulin sensitivity
Convenient once-weekly dosing

Is Semaglutide Safe?
Semaglutide is a safe, NHB-approved medication with minimal side effects.

Benefits of AOD 9604
Fat doesn’t stand a chance against this naturally powerful peptide, whose impressive fat-fighting abilities can provide the following benefits, such as:

Reduces body fat
Increases calorie burn
Triggers fat release>
Boosts your metabolism
Prevents non-fatty foods from turning into body fat
Doesn’t increase your appetite

A weight loss breakthrough.
Recent scientific discoveries offer insight into how our metabolism and hormones change over time — and how that impacts whether we’ll gain or lose weight. It comes down to the relationship between our brains and our guts.

A new family of medications called GLP-1s address these biological factors head-on. THE TRUTH IS...
It's not about willpower.
It's biology.
Up to 70% of weight gain is linked to genetics. On top of that, other health conditions and medications can make weight loss even more difficult.

And the environment we live in can influence our access to affordable and reliable healthcare and nutrition.

Peptide GLP-1s fight back against these genetic, biological, and environmental factors that prevent weight loss.
244 genes linked to obesity
BOOSTING YOUR BODY'S NATURAL ABILITIES
How GLP-1s Work
WHAT

A naturally occurring hormone
GLP-1 is naturally released by the gut in response to food.

HOW

An extra boost for your system
The effects include increasing insulin release from the pancreas, slowing down stomach emptying, and targeting receptors in the brain that cause appetite reduction.

RESULT

A more efficient weight loss outcome
This results in a sensation of satiety, or fullness, lasting much longer than possible with natural GLP-1 hormone levels.
Other medications
Your Brightpath Clinician may determine that another medication or a combination of medications might work best for your medical history and biology. They will do a careful review of your specific case to ensure you’re getting an effective medication that meets your needs.

You can learn more about different medications, common side effects, and their results and costs, by call us today for a free consultation at 480-317-SLIM

Here is a layout that I woukd like inside on the bottom half

Went on vacation/holiday

Target Market(s)

anyone with a BMI over28

Industry/Entity Type

medical weight loss

Requirements
Must have
• call to action
Nice to have
• include 5 star review
Should not have
• too many words

```html
<!DOCTYPE html>
<html lang="en">
<head>
<meta charset="utf-8">
<title>Peptide Weight Loss Flyer</title>
<link rel="stylesheet" href="https://fonts.googleapis.com/css2?family=Archivo+Black&family=Archivo:wght@500;700;800&display=swap">
<style>
  :root {
    --stage: #e8edf0;
    --sky-top: #86b0cc;
    --sky-mid: #cfe0ec;
    --sky-low: #b9d2e4;
    --red: #c8151b;
    --red-deep: #a30f14;
    --ink: #111418;
    --ink-soft: #1f2a33;
    --white: #ffffff;
    --pale-blue: #9fc2dc;
    --photo-a: #d9c2ae;
    --photo-b: #4f6f92;
  }
  * { margin: 0; padding: 0; box-sizing: border-box; }
  html, body { width: 1200px; height: 800px; overflow: hidden; }
  body { background: var(--stage); font-family: "Archivo", Arial, sans-serif; position: relative; }

  .flyer {
    position: absolute; left: 320px; top: 20px; width: 560px; height: 760px;
    background: linear-gradient(180deg, var(--sky-top) 0%, var(--sky-mid) 45%, var(--sky-low) 100%);
    box-shadow: 0 6px 22px rgba(0,0,0,.25);
    overflow: hidden; color: var(--ink);
  }

  .photo { position: absolute; left: 0; top: 210px; width: 196px; height: 470px;
    background: linear-gradient(180deg, var(--photo-a) 0%, var(--photo-a) 48%, var(--photo-b) 72%, var(--photo-b) 100%); opacity: .85; }

  .brand { position: absolute; left: 26px; top: 40px; font-family: "Archivo Black", Arial, sans-serif; line-height: .95; }
  .brand-peptide { color: var(--red); font-size: 34px; letter-spacing: .5px; }
  .brand-sub { color: var(--ink); font-size: 19px; }

  .content { position: absolute; left: 214px; top: 44px; width: 318px; display: flex; flex-direction: column; }

  .headline-main { font-family: "Archivo Black", Arial, sans-serif; font-size: 16px; line-height: 21px; text-transform: uppercase; font-weight: 400; }
  .headline-product { font-family: "Archivo Black", Arial, sans-serif; color: var(--red); font-size: 21px; line-height: 26px; margin-top: 4px; font-weight: 400; }
  .intro { margin-top: 4px; font-weight: 800; font-size: 6.8px; line-height: 9px; text-transform: uppercase; }

  .label { display: flex; align-items: flex-end; margin: 6px 0 5px; }
  .label-box { background: var(--red); color: var(--white); font-family: "Archivo Black", Arial, sans-serif; font-size: 11px; line-height: 11px; padding: 2px 10px 2px 10px; text-transform: uppercase; white-space: nowrap; }
  .label-rule { height: 2px; background: var(--ink); width: 60px; }
  .label-right { justify-content: flex-end; }

  .list { list-style: none; font-weight: 700; font-size: 6px; line-height: 8px; text-transform: uppercase; color: var(--ink-soft); }
  .list li { display: flex; gap: 7px; align-items: flex-start; margin-bottom: 3px; }
  .list li:last-child { margin-bottom: 0; }
  .list svg { flex: none; margin-top: 0; }
  .list-checks { padding-left: 6px; }
  .list-bullets { padding-left: 10px; }
  .list-bullets li::before, .list-right li::after { content: ""; width: 4px; height: 4px; background: var(--ink); flex: none; margin-top: 2px; }
  .list-right { text-align: right; padding-right: 6px; }
  .list-right li { justify-content: flex-end; }

  .dateline { text-align: right; font-weight: 700; font-size: 6px; line-height: 8px; text-transform: uppercase; margin-top: 3px; padding-right: 6px; }

  .aod-intro { align-self: flex-end; width: 270px; text-align: right; font-weight: 700; font-size: 6px; line-height: 8px; text-transform: uppercase; margin-bottom: 4px; padding-right: 6px; }

  .reviews { margin-left: -56px; text-align: right; font-weight: 700; font-size: 6px; line-height: 8px; text-transform: uppercase; padding-right: 4px; }
  .reviews p { margin-bottom: 3px; }

  .footer-art { position: absolute; left: 0; top: 660px; }
  .safe-note { position: absolute; left: 16px; top: 700px; width: 200px; color: var(--white); font-weight: 800; font-size: 8.2px; line-height: 11px; text-transform: uppercase; }
  .cta { position: absolute; left: 236px; top: 674px; width: 310px; color: var(--white); font-weight: 700; font-size: 6.8px; line-height: 9.2px; text-transform: uppercase; text-align: center; }
</style>
</head>
<body>
<main class="flyer">
  <div class="photo" role="img" aria-label="Photo of a smiling slim woman in a black crop top giving a thumbs up while holding out the waistband of oversized jeans"></div>

  <div class="brand">
    <div class="brand-peptide">PEPTIDE</div>
    <div class="brand-sub">WEIGHT LOSS</div>
  </div>

  <div class="content">
    <h1 class="headline-main">A new and very effortless way to loose weight and keep it off!!</h1>
    <h2 class="headline-product">SEMAGLUTIDE &amp; AOD9604</h2>
    <p class="intro">(We also have Vitalis Core, a product that heals the gut biome and brain hormone response to weight loss. These three items stacked together is what sets us apart from other clinics. Both peptides are approved by the NHB for weight loss.)</p>

    <div class="label"><span class="label-box">What we do</span><span class="label-rule"></span></div>
    <ul class="list list-checks">
      <li><svg width="7" height="7" viewBox="0 0 8 8"><rect x=".5" y=".5" width="7" height="7" fill="none" stroke="#111418"/><path d="M1.5 4l2 2 3.5-5" fill="none" stroke="#111418" stroke-width="1.2"/></svg>We also compound our peptides so they are much cheaper than the commercial semaglutide also known as Lunavex and Trelmo.</li>
      <li><svg width="7" height="7" viewBox="0 0 8 8"><rect x=".5" y=".5" width="7" height="7" fill="none" stroke="#111418"/><path d="M1.5 4l2 2 3.5-5" fill="none" stroke="#111418" stroke-width="1.2"/></svg>These two commercial peptides from big pharma, each run about 1200.00 per month. That cost.</li>
      <li><svg width="7" height="7" viewBox="0 0 8 8"><rect x=".5" y=".5" width="7" height="7" fill="none" stroke="#111418"/><path d="M1.5 4l2 2 3.5-5" fill="none" stroke="#111418" stroke-width="1.2"/></svg>Our compounded peptides are a fraction of that cost.</li>
      <li><svg width="7" height="7" viewBox="0 0 8 8"><rect x=".5" y=".5" width="7" height="7" fill="none" stroke="#111418"/><path d="M1.5 4l2 2 3.5-5" fill="none" stroke="#111418" stroke-width="1.2"/></svg>AOD9604....(Anti obesity drug)</li>
      <li><svg width="7" height="7" viewBox="0 0 8 8"><rect x=".5" y=".5" width="7" height="7" fill="none" stroke="#111418"/><path d="M1.5 4l2 2 3.5-5" fill="none" stroke="#111418" stroke-width="1.2"/></svg>Patients are losing as much weight as if they had bariatric surgery. 3-5 pounds per week.</li>
    </ul>
    <p class="dateline">Added Wednesday, 22 February 2023</p>

    <div class="label"><span class="label-box">Benefits of semaglutide:</span><span class="label-rule"></span></div>
    <ul class="list list-bullets">
      <li>Reduces hunger pangs</li>
      <li>Makes you feel fuller longer</li>
      <li>Reduces food cravings</li>
      <li>Reduces cardiovascular risk factors</li>
      <li>Improves insulin sensitivity</li>
      <li>Convenient once weekly dosing</li>
    </ul>

    <div class="label label-right"><span class="label-rule"></span><span class="label-box">Benefits of AOD 9604</span></div>
    <p class="aod-intro">Fat doesn't stand a chance against this naturally powerful peptide, whose impressive fat-fighting abilities can provide the following benefits, such as:</p>
    <ul class="list list-right">
      <li>Reduces body fat</li>
      <li>Increases calorie burn</li>
      <li>Triggers fat release</li>
      <li>Boosts your metabolism</li>
      <li>Prevents non-fatty foods from turning into body fat</li>
      <li>Doesn't increase your appetite</li>
    </ul>

    <div class="label label-right"><span class="label-rule"></span><span class="label-box">Five star reviews</span></div>
    <section class="reviews">
      <p>"I have been on semaglutide for one month. I guess the numbers are the crucial part of all semaglutide reviews. That's it. I have dropped 16lbs. One of the things I have truly come to appreciate is that Sem will limit your appetite." Marisol</p>
      <p>"I've lost 13.5 pounds in a month, and I can't even tell how it happened. The interesting part is that I don't want to eat sweets anymore. I just want to eat less. I eat small portions while losing weight and enjoy my life." Tansy47</p>
      <p>"I've been on the double peptide plan for a month and have dropped 20 pounds, despite not exercising. I'm delighted to see these figures change." Wendell</p>
      <p>"Semaglutide worked for me. 10 out of 10." Gus<br>Added Wednesday, 22 February 2023</p>
      <p>Hunger pangs! The primary roadblock to weight loss. With semaglutide, hunger pangs are a thing of the past. Semaglutide....changing the game!</p>
    </section>
  </div>

  <svg class="footer-art" width="560" height="100" viewBox="0 0 560 100" aria-hidden="true">
    <rect x="0" y="28" width="230" height="72" fill="#9fc2dc"/>
    <polygon points="232,10 560,0 560,52 212,62" fill="#c8151b"/>
    <polygon points="212,62 560,52 560,56 211,66" fill="#a30f14"/>
  </svg>
  <p class="safe-note">Is semaglutide safe?<br>Semaglutide is a safe, NHB-approved medication with minimal side effects.<br>Added Wednesday, 22 February 2023</p>
  <p class="cta">If your are like 85% of dieters, its not your first time trying to get healthy and lose weight. Join thousands of folks pushing the past plateaus and kill the cravings without starving via Quarlin MD's 16-week program.</p>
</main>
</body>
</html>
```